Modern Homepage Design for brenvik.nl – Fish & Chicken Food Webshop

Brenvik.nl is an online store that sells fish and chicken food. The design should be visually appealing, easy to navigate, and optimized for e-commerce. We want a layout that helps customers quickly find what they need and encourages them to explore our products.
A good example of the style and structure we like is dierkamp.nl – clean layout, clear product focus, and user-friendly navigation.
Brand Colors (must be used):
Orange: #f7a441
Dark Gray: #3c3c3b
White: #ffffff
Please use these colors consistently throughout the design.
Homepage Requirements:
The homepage should include the following sections:
Main Slider / Hero Banner
A large, eye-catching slider at the top of the page to highlight promotions or featured categories.
Category Blocks
A section with clear, clickable blocks or tiles that link to main product categories (e.g., Fish Food, Chicken Food, Accessories).
Featured Products
A section showcasing selected or best-selling products.
Special Offers / Promotions
A space to highlight current deals or limited-time offers.
Three Banners in a Row
A section with three horizontal banners side by side, which can be used for promotions, shipping info, or other key messages.
Unique Selling Points (USPs)
A section that briefly explains what makes our store different (e.g., fast delivery, high-quality feed, trusted by professionals).
SEO Content Block
A short paragraph of text for SEO purposes (use Lorem Ipsum for dummy content).
Footer Design
Include space for contact information, navigation links, and social media.
Design Notes:
The design must be responsive and mobile-friendly.
Focus on clean layout, good spacing, and easy navigation.
Use modern fonts and a clear visual hierarchy.
We are only looking for the homepage design at this stage, but we may work with the selected designer on additional pages later.
Deliverables:
Homepage design in layered PSD, Figma, or Adobe XD format
Any fonts and assets used
Preview images/mockups
We look forward to seeing your ideas and working with a designer who can bring our brand to life with a fresh and functional homepage design.
Let us know if you have any questions.
Hobby Animal Keepers, Pet Owners
Animal Nutrition & Feed
2 page

```html
<!DOCTYPE html>
<html lang="en">
<head>
<meta charset="utf-8">
<title>Brenvik.nl – Fish &amp; Chicken Food</title>
<link href="https://fonts.googleapis.com/css2?family=Oswald:wght@500;700&family=Poppins:wght@400;500;600&display=swap" rel="stylesheet">
<style>
:root{
  --orange:#f7a441;
  --orange-deep:#ec9c3b;
  --dark:#3c3c3b;
  --ink:#232323;
  --black:#262626;
  --peach:#fde8cd;
  --peach-soft:#fdf0e0;
  --card-grey:#f3f3f3;
  --white:#ffffff;
  --muted:#555;
}
*{box-sizing:border-box;margin:0;padding:0}
html,body{width:1200px;height:3518px;overflow:hidden}
body{position:relative;background:var(--white);font-family:"Poppins",sans-serif;color:var(--ink)}
.abs{position:absolute}
.head{font-family:"Oswald",sans-serif;font-weight:700;text-transform:uppercase;letter-spacing:.2px}

.topbar{left:0;top:0;width:1200px;height:38px;background:var(--black);color:#fff;font-size:12px;display:flex;align-items:center;justify-content:center;gap:8px}
.header{left:0;top:38px;width:1200px;height:110px;background:var(--peach)}
.logo{left:160px;top:30px;display:flex;align-items:center;gap:8px;font-family:"Poppins",sans-serif;font-weight:600;font-size:36px;color:var(--dark)}
.logo-dot{width:30px;height:30px;border-radius:50%;background:var(--orange)}
.search{left:416px;top:36px;width:504px;height:36px;border-radius:18px;background:#fff;border:1px solid #ddd;font-size:11px;color:#777;display:flex;align-items:center;padding-left:16px;gap:8px}
.account{left:812px;top:36px;width:108px;height:36px;border-radius:18px;border:1px solid #555;background:#fff;font-size:13px;display:flex;align-items:center;justify-content:center;gap:6px}
.cart{left:960px;top:44px;font-family:"Oswald",sans-serif;font-weight:500;font-size:13px;display:flex;gap:8px;align-items:center}
.nav{left:0;top:148px;width:1200px;height:43px;background:var(--orange-deep);display:flex;justify-content:center;align-items:center;gap:66px;font-family:"Oswald",sans-serif;font-weight:500;font-size:12px;color:#fff}

.hero{left:98px;top:252px;width:1002px;height:290px;border-radius:14px;background:var(--orange);overflow:hidden}
.hero h1{left:62px;top:30px;font-size:56px;line-height:66px;color:#fff}
.hero p{left:62px;top:166px;font-size:13px;line-height:16px;color:#fff}
.btn-dark{background:var(--black);color:#fff;border-radius:20px;font-family:"Oswald",sans-serif;font-weight:500;font-size:12px;display:flex;align-items:center;justify-content:center}
.hero-photo{left:544px;top:0;width:458px;height:290px;background:linear-gradient(120deg,#e9a04a 0%,#b98a53 30%,#5b4a3a 60%,#2b2622 100%);clip-path:polygon(18% 0,100% 0,100% 100%,0 100%)}

.cat{top:602px;width:268px;height:317px;border-radius:18px;background:var(--card-grey);text-align:center}
.cat.active{background:#fff;border:3px solid var(--orange)}
.cat .kicker{margin-top:26px;font-family:"Oswald",sans-serif;font-weight:500;font-size:28px;color:transparent;-webkit-text-stroke:1px #777}
.cat.active .kicker{-webkit-text-stroke:1px var(--orange)}
.cat .title{font-size:44px;line-height:48px;color:var(--ink)}
.cat.active .title{color:var(--orange)}
.cat .pic{margin:24px auto 0;width:190px;height:170px;border-radius:12px}

.featured-bg{left:0;top:965px;width:1200px;height:760px}
.section-title{width:1200px;left:0;text-align:center;font-size:38px;color:var(--ink)}
.prod{top:1162px;width:242px;height:319px;border:3px solid var(--orange);border-radius:8px;background:#fff;text-align:center}
.prod.hover{border:none;box-shadow:0 12px 30px rgba(0,0,0,.12)}
.prod .pack{margin:30px auto 0;width:80px;height:140px;border-radius:8px}
.stars{margin-top:24px;font-size:15px;color:var(--orange);letter-spacing:1px}
.stars span{color:#555;font-size:11px;margin-left:4px}
.prod .name{margin-top:14px;font-family:"Oswald",sans-serif;font-weight:700;font-size:24px}
.prod .price{margin-top:4px;font-family:"Oswald",sans-serif;font-weight:500;font-size:13px}
.add{left:642px;top:1462px;width:182px;height:36px;border:1px solid var(--orange);border-radius:18px;background:#fff;color:var(--orange);font-family:"Oswald",sans-serif;font-weight:500;font-size:13px;display:flex;align-items:center;justify-content:center}
.dots{left:572px;top:1532px;display:flex;gap:7px}
.dots i{width:8px;height:8px;border-radius:50%;background:#777;display:block}
.dots i.on{background:var(--orange)}
.btn-orange{background:var(--orange-deep);color:#fff;border-radius:20px;font-family:"Oswald",sans-serif;font-weight:500;font-size:12px;display:flex;align-items:center;justify-content:center}

.deal{left:161px;top:1770px;width:876px;height:344px;border-radius:18px;overflow:hidden;background:#f8dcbd}
.deal h2{left:58px;top:96px;font-size:58px;color:var(--ink)}
.deal p{left:60px;top:176px;font-size:13px;line-height:17px;color:#333}
.deal-photo{left:500px;top:0;width:376px;height:344px;background:linear-gradient(110deg,#e9a96b 0%,#c7683a 35%,#5b2f1f 70%,#231915 100%);clip-path:polygon(8% 0,100% 0,100% 100%,0 100%)}

.promo{top:2144px;width:285px;height:141px;background:var(--peach-soft);overflow:hidden;box-shadow:0 6px 14px rgba(0,0,0,.08)}
.promo .txt{left:20px;top:32px;font-family:"Oswald",sans-serif;font-weight:700;font-size:21px;line-height:27px;color:var(--ink);text-transform:uppercase}
.promo .txt em{font-style:normal;color:var(--orange)}
.promo .pic{right:0;top:0;width:120px;height:141px;background:linear-gradient(160deg,#f7a441,#e07a2a 60%,#c6532a);clip-path:polygon(35% 0,100% 0,100% 100%,0 100%)}
.promo .arrow{right:14px;top:104px;width:26px;height:26px;border-radius:50%;background:var(--ink);display:flex;align-items:center;justify-content:center}

.why-title{top:2400px;color:#fff}
.why-sub{left:0;width:1200px;top:2462px;text-align:center;color:#fff;font-size:14px;line-height:18px}
.usp{top:2530px;display:flex;align-items:center;gap:10px;font-family:"Oswald",sans-serif;font-weight:700;font-size:22px;line-height:26px;color:#fff}
.hero-animals{left:416px;top:2582px;width:318px;height:238px;border-radius:50%;background:radial-gradient(circle at 40% 55%,#ec6b2d 0%,#c7572a 45%,#8d4a2d 75%,rgba(141,74,45,0) 100%)}

.seo-title{top:2868px;color:var(--ink)}
.seo p{left:256px;width:688px;text-align:center;font-size:14px;line-height:20px;color:#333}

.footer{left:0;top:3146px;width:1200px;height:372px}
.news-h{left:161px;top:3268px;font-family:"Oswald",sans-serif;font-weight:500;font-size:19px;color:#fff}
.news-p{left:161px;top:3296px;font-size:11px;color:#ddd}
.news-form{left:600px;top:3272px;width:438px;height:40px;border-radius:20px;background:#fff;overflow:hidden;display:flex}
.news-form span{flex:1;font-size:12px;color:#666;display:flex;align-items:center;padding-left:14px}
.news-form b{width:102px;background:var(--orange);color:#fff;font-family:"Oswald",sans-serif;font-weight:500;font-size:13px;display:flex;align-items:center;justify-content:center}
.rule{left:161px;width:876px;height:1px;background:#4a4a4a}
.flinks{left:161px;top:3386px;display:flex;gap:58px;font-size:15px;color:#fff}
.flinks .cur{color:var(--orange)}
.social{left:934px;top:3388px;display:flex;gap:28px}
.social i{width:14px;height:14px;border-radius:50%;border:2px solid #fff;display:block}
.pay{left:502px;top:3468px;display:flex;gap:8px}
.pay span{width:44px;height:30px;border-radius:3px;background:#2d5cae;color:#fff;font-size:10px;font-weight:600;display:flex;align-items:center;justify-content:center}
</style>
</head>
<body>

<div class="abs topbar">
  <svg width="14" height="14" viewBox="0 0 24 24"><path fill="#fff" d="M6.6 10.8a15 15 0 006.6 6.6l2.2-2.2c.3-.3.7-.4 1-.2 1.1.4 2.3.6 3.6.6.6 0 1 .4 1 1V20c0 .6-.4 1-1 1C10.6 21 3 13.4 3 4c0-.6.4-1 1-1h3.5c.6 0 1 .4 1 1 0 1.3.2 2.5.6 3.6.1.3 0 .7-.2 1z"/></svg>
  Questions? 085-0123456
</div>

<div class="abs header">
  <div class="abs logo"><span class="logo-dot"></span>brenvik</div>
  <div class="abs search">
    <svg width="14" height="14" viewBox="0 0 24 24"><circle cx="10" cy="10" r="7" fill="none" stroke="#333" stroke-width="2"/><path d="M15 15l6 6" stroke="#333" stroke-width="2"/></svg>
    Search for...
  </div>
  <div class="abs account">
    <svg width="13" height="13" viewBox="0 0 24 24"><circle cx="12" cy="8" r="4" fill="none" stroke="#333" stroke-width="2"/><path d="M4 21c1-4 4-6 8-6s7 2 8 6" fill="none" stroke="#333" stroke-width="2"/></svg>
    Account
  </div>
  <div class="abs cart">
    <svg width="18" height="16" viewBox="0 0 24 22"><path d="M1 2h4l3 12h12l3-9H7" fill="none" stroke="#333" stroke-width="2"/><circle cx="10" cy="19" r="2" fill="#333"/><circle cx="18" cy="19" r="2" fill="#333"/></svg>
    $0.00 (0)
  </div>
</div>

<nav class="abs nav">
  <span>HOME</span><span>ABOUT</span><span>FISHING</span><span>CHICKENS</span><span>CATEGORIES</span><span>CONTACT US</span>
</nav>

<section class="abs hero">
  <div class="abs hero-photo" role="img" aria-label="Fish food packs beside a striped tropical fish on gravel"></div>
  <h1 class="abs head">Premium Hemp &amp;<br>THCA Products</h1>
  <p class="abs">Quality hemp products from trusted Oregon farms,<br>third-party tested for purity.</p>
  <div class="abs btn-dark" style="left:62px;top:214px;width:160px;height:36px">SHOP NOW</div>
</section>

<div class="abs cat active" style="left:160px">
  <div class="kicker">FISH</div>
  <div class="title head">Food</div>
  <div class="pic" role="img" aria-label="Orange goldfish" style="background:radial-gradient(ellipse at 50% 55%,#f07a3a 0%,#f5a36b 40%,rgba(255,255,255,0) 72%)"></div>
</div>
<div class="abs cat" style="left:465px">
  <div class="kicker">CHICKEN</div>
  <div class="title head">Food</div>
  <div class="pic" role="img" aria-label="Grey chicken" style="background:radial-gradient(ellipse at 50% 55%,#777 0%,#aaa 40%,rgba(243,243,243,0) 72%)"></div>
</div>
<div class="abs cat" style="left:770px">
  <div class="kicker">FOOD</div>
  <div class="title head">Accessories</div>
  <div class="pic" role="img" aria-label="Jar of fish pellets" style="width:80px;background:linear-gradient(#555,#222)"></div>
</div>

<svg class="abs featured-bg" viewBox="0 0 1200 760" preserveAspectRatio="none" aria-hidden="true">
  <path d="M0 0 Q600 110 1200 0 V760 Q600 650 0 760 Z" fill="#fdebd4"/>
</svg>

<h2 class="abs head section-title" style="top:1072px">Featured Products</h2>

<div class="abs prod" style="left:71px">
  <div class="pack" role="img" aria-label="Flake food tin" style="background:linear-gradient(#f2c230,#1d4d8a 40%,#15345f)"></div>
  <div class="stars">★★★★★<span>(10)</span></div>
  <div class="name">AquaMin Flake</div>
  <div class="price">$80.60</div>
</div>
<div class="abs prod" style="left:341px">
  <div class="pack" role="img" aria-label="Chicken feed pouch" style="background:linear-gradient(#f0e5d4,#f29a3e 55%,#e8d8c2)"></div>
  <div class="stars">★★★★★<span>(10)</span></div>
  <div class="name">Hearty Hen Mix</div>
  <div class="price">$80.60</div>
</div>
<div class="abs prod hover" style="left:613px">
  <div class="pack" role="img" aria-label="Jar of fish pellets" style="width:64px;background:linear-gradient(#a8341f,#2a2a2a 35%,#1a1a1a)"></div>
  <div class="stars">★★★★★<span>(10)</span></div>
  <div class="name">Marlo Basic</div>
  <div class="price">$80.60</div>
</div>
<div class="abs prod" style="left:883px">
  <div class="pack" role="img" aria-label="Protein food pouch" style="width:92px;background:linear-gradient(#9fdcef,#e7d6ea 50%,#b03b9b)"></div>
  <div class="stars">★★★★★<span>(10)</span></div>
  <div class="name">Regal Koi</div>
  <div class="price">$80.60</div>
</div>
<div class="abs add">Add To Cart</div>

<div class="abs dots"><i></i><i></i><i class="on"></i><i></i></div>
<div class="abs btn-orange" style="left:512px;top:1570px;width:174px;height:36px">VIEW ALL PRODUCTS</div>

<section class="abs deal">
  <div class="abs deal-photo" role="img" aria-label="Goldfish among bubbles with feed packs"></div>
  <h2 class="abs head">Deal of the Week</h2>
  <p class="abs">Quality hemp products from trusted Oregon farms,<br>third-party tested for purity.</p>
  <div class="abs btn-orange" style="left:60px;top:226px;width:160px;height:36px">SHOP NOW</div>
</section>

<div class="abs promo" style="left:161px">
  <div class="abs pic" role="img" aria-label="Fish food jars"></div>
  <div class="abs txt"><em>Nutrition</em><br>For growth<br>&amp; colour.</div>
  <div class="abs arrow"><svg width="12" height="10" viewBox="0 0 12 10"><path d="M0 5h10M6 1l4 4-4 4" fill="none" stroke="#fff" stroke-width="1.5"/></svg></div>
</div>
<div class="abs promo" style="left:456px">
  <div class="abs pic" role="img" aria-label="Chicken feed pouches"></div>
  <div class="abs txt" style="top:44px"><em>Save big</em><br>Shop big</div>
  <div class="abs arrow"><svg width="12" height="10" viewBox="0 0 12 10"><path d="M0 5h10M6 1l4 4-4 4" fill="none" stroke="#fff" stroke-width="1.5"/></svg></div>
</div>
<div class="abs promo" style="left:753px">
  <div class="abs pic" role="img" aria-label="Protein food pouches" style="background:linear-gradient(160deg,#f7a441,#e07a2a)"></div>
  <div class="abs txt" style="top:44px"><em>Save on</em><br>Final<br>frights</div>
  <div class="abs arrow"><svg width="12" height="10" viewBox="0 0 12 10"><path d="M0 5h10M6 1l4 4-4 4" fill="none" stroke="#fff" stroke-width="1.5"/></svg></div>
</div>

<svg class="abs" style="left:0;top:2353px" width="1200" height="300" viewBox="0 0 1200 300" preserveAspectRatio="none" aria-hidden="true">
  <path d="M0 0H1200V292Q600 220 0 292Z" fill="#f7a441"/>
</svg>
<h2 class="abs head section-title why-title">Why Choose Us</h2>
<p class="abs why-sub">We're here at Brenvik to ensure that you have the best possible<br>experience with the highest quality products.</p>

<div class="abs usp" style="left:210px;top:2540px">
  <svg width="64" height="40" viewBox="0 0 64 40"><path d="M14 4h30v24H14zM44 12h10l6 8v8H44z" fill="#fff"/><circle cx="24" cy="32" r="5" fill="#fff" stroke="#f7a441" stroke-width="2"/><circle cx="52" cy="32" r="5" fill="#fff" stroke="#f7a441" stroke-width="2"/><path d="M0 10h10M2 16h10M4 22h8" stroke="#fff" stroke-width="2"/></svg>
  Fast Delivery
</div>
<div class="abs usp" style="left:504px;top:2536px">
  <svg width="32" height="46" viewBox="0 0 32 46"><circle cx="16" cy="16" r="13" fill="none" stroke="#fff" stroke-width="3"/><path d="M16 9l2.3 4.7 5.2.7-3.8 3.6.9 5.1-4.6-2.4-4.6 2.4.9-5.1-3.8-3.6 5.2-.7z" fill="#fff"/><path d="M8 27l-3 16 6-3 4 5 1-12M24 27l3 16-6-3-4 5" fill="none" stroke="#fff" stroke-width="2.5"/></svg>
  High-Qality Feed
</div>
<div class="abs usp" style="left:810px;top:2526px">
  <svg width="40" height="46" viewBox="0 0 40 46"><circle cx="24" cy="9" r="7" fill="#fff"/><path d="M12 44V28c0-6 5-10 12-10s12 4 12 10v16z" fill="#fff"/><circle cx="10" cy="32" r="9" fill="#f7a441" stroke="#fff" stroke-width="2.5"/><path d="M5 32l4 4 6-7" fill="none" stroke="#fff" stroke-width="2.5"/></svg>
  Trusted By<br>Professionals
</div>

<div class="abs hero-animals" role="img" aria-label="Orange fish swimming beside a rooster"></div>

<h2 class="abs head section-title seo-title">Lorem Ipsum</h2>
<div class="seo">
  <p class="abs" style="top:2950px">Lorem Ipsum is simply dummy text of the printing and typesetting industry. Lorem Ipsum has been the industry's standard dummy text ever since the 1500s, when an unknown printer took a galley of type and scrambled it to make a type specimen book.</p>
  <p class="abs" style="top:3028px">Lorem Ipsum is simply dummy text of the printing and typesetting industry. Lorem Ipsum has been the industry's standard dummy text ever since the 1500s, when an unknown printer took a galley of type and scrambled it to make a type specimen book.</p>
</div>
<div class="abs btn-orange" style="left:513px;top:3118px;width:174px;height:35px">LEARN MORE</div>

<footer>
  <svg class="abs footer" viewBox="0 0 1200 372" preserveAspectRatio="none" aria-hidden="true">
    <path d="M0 0Q600 120 1200 0V372H0Z" fill="#f7a441"/>
    <path d="M0 14Q600 134 1200 14V372H0Z" fill="#262626"/>
  </svg>
  <div class="abs news-h">SIGN UP FOR OUR NEWSLETTER</div>
  <div class="abs news-p">Give your inbox some love with new products tips, &amp; more.</div>
  <div class="abs news-form"><span>Enter Email Address</span><b>SUBSCRIBE</b></div>
  <div class="abs rule" style="top:3345px"></div>
  <div class="abs flinks"><span class="cur">Home</span><span>Fishing</span><span>Chickens</span><span>Categories</span><span>Blog</span><span>Contact Us</span></div>
  <div class="abs social" aria-label="Social links"><i></i><i></i><i></i></div>
  <div class="abs rule" style="top:3451px"></div>
  <div class="abs pay"><span>Paylo</span><span>Vora</span><span>Cardo</span><span>Exmo</span></div>
</footer>

</body>
</html>
```